Bright Oak Fitness Facility Business Cards

Business Card Design that incorporates the logo and tagline

Target Market(s)

Fitness, People Who Exercise

Contact Information for Business Card

2817 Mossgrove Bend Road
Tavares, Florida 32190
Phone: 352-555-Jump (5867)
www.brightoakfitness.example
info@brightoakfitness.example

Requirements
Must have
• Logo, Address, Website, email and tagline "More Than A Gym". Colors should be red/black/grey/white

```html
<!DOCTYPE html>
<html lang="en">
<head>
<meta charset="utf-8">
<title>Bright Oak Fitness Facility – Business Card</title>
<link rel="stylesheet" href="https://fonts.googleapis.com/css2?family=Montserrat:wght@600;700&family=Arimo:wght@400&display=swap">
<style>
  :root {
    --brand-red: #e3151b;
    --ink: #111111;
    --link-blue: #1b2f9c;
    --card-border: #333333;
    --page: #ffffff;
  }
  html, body {
    margin: 0;
    padding: 0;
    width: 1200px;
    height: 1200px;
    overflow: hidden;
    background: var(--page);
  }
  .canvas {
    position: relative;
    width: 1200px;
    height: 1200px;
  }
  .business-card {
    position: absolute;
    left: 48px;
    top: 262px;
    width: 1102px;
    height: 676px;
    box-sizing: border-box;
    border: 2px solid var(--card-border);
    background: var(--page);
    overflow: hidden;
  }
  .brand-mark {
    position: absolute;
    left: 232px;
    top: 222px;
    width: 80px;
    height: 80px;
    border-radius: 50%;
    background: var(--brand-red);
  }
  .brand-name {
    position: absolute;
    left: 20px;
    top: 340px;
    width: 510px;
    margin: 0;
    text-align: center;
    font-family: "Montserrat", sans-serif;
    font-weight: 700;
    font-size: 76px;
    line-height: 1;
    letter-spacing: -1px;
    color: var(--ink);
    white-space: nowrap;
  }
  .tagline {
    position: absolute;
    left: 22px;
    top: 437px;
    width: 510px;
    margin: 0;
    display: flex;
    align-items: center;
    gap: 12px;
    font-family: "Montserrat", sans-serif;
    font-weight: 700;
    font-size: 19px;
    color: var(--ink);
    white-space: nowrap;
  }
  .tagline::before,
  .tagline::after {
    content: "";
    flex: 1;
    height: 3px;
    background: var(--ink);
  }
  .divider {
    position: absolute;
    left: 550px;
    top: 32px;
    width: 3px;
    height: 612px;
    background: var(--ink);
    border-radius: 2px;
  }
  .contact-list {
    position: absolute;
    left: 564px;
    top: 222px;
    width: 520px;
    margin: 0;
    padding: 0;
    list-style: none;
    font-family: "Arimo", sans-serif;
    font-size: 31px;
    line-height: 44px;
  }
  .contact-item {
    display: flex;
    align-items: flex-start;
  }
  .contact-icon {
    width: 44px;
    height: 44px;
    flex: none;
    margin-right: 14px;
  }
  .contact-text {
    color: var(--link-blue);
    text-decoration: underline;
    text-decoration-thickness: 2px;
    text-underline-offset: 3px;
    white-space: nowrap;
  }
  .contact-text--plain {
    color: var(--ink);
    text-decoration: none;
  }
</style>
</head>
<body>
<main class="canvas">
  <section class="business-card" aria-label="Bright Oak Fitness Facility business card">
    <div class="brand-mark" aria-hidden="true"></div>
    <h1 class="brand-name">BRIGHT OAK</h1>
    <p class="tagline">MORE THAN A GYM</p>

    <div class="divider" aria-hidden="true"></div>

    <ul class="contact-list">
      <li class="contact-item">
        <svg class="contact-icon" viewBox="0 0 44 44" aria-hidden="true">
          <circle cx="22" cy="22" r="18" fill="none" stroke="var(--brand-red)" stroke-width="4"/>
          <path d="M12 22 L22 13 L32 22 H28 V30 H16 V22 Z" fill="var(--brand-red)"/>
          <rect x="20" y="24" width="4" height="6" fill="#fff"/>
        </svg>
        <span class="contact-text">2817 Mossgrove Bend Road<br>Tavares, Florida 32190</span>
      </li>
      <li class="contact-item">
        <svg class="contact-icon" viewBox="0 0 44 44" aria-hidden="true">
          <circle cx="22" cy="22" r="18" fill="none" stroke="var(--brand-red)" stroke-width="4"/>
          <path d="M16 13 L20 12 L22 18 L19 20 C20 23 22 25 25 26 L27 23 L32 25 L31 29 C25 31 14 21 16 13 Z" fill="var(--brand-red)"/>
        </svg>
        <span class="contact-text">352-555-Jump (5867)</span>
      </li>
      <li class="contact-item">
        <svg class="contact-icon" viewBox="0 0 44 44" aria-hidden="true">
          <circle cx="22" cy="22" r="18" fill="none" stroke="var(--brand-red)" stroke-width="4"/>
          <rect x="12" y="16" width="20" height="13" fill="none" stroke="var(--brand-red)" stroke-width="2.5"/>
          <path d="M12 16 L22 24 L32 16" fill="none" stroke="var(--brand-red)" stroke-width="2.5"/>
        </svg>
        <span class="contact-text">www.brightoakfitness.example</span>
      </li>
      <li class="contact-item">
        <svg class="contact-icon" viewBox="0 0 44 44" aria-hidden="true">
          <circle cx="22" cy="22" r="18" fill="none" stroke="var(--brand-red)" stroke-width="4"/>
          <path d="M22 31 C18 26 16 22 16 19 A6 6 0 0 1 28 19 C28 22 26 26 22 31 Z" fill="var(--brand-red)"/>
          <circle cx="22" cy="19" r="2.2" fill="#fff"/>
        </svg>
        <span class="contact-text contact-text--plain">info@brightoakfitness.example</span>
      </li>
    </ul>
  </section>
</main>
</body>
</html>
```